Business Card and Letterhead for Nurlo - modern real estate business

I need a double sided business card design for Nurlo. Please see business card brief here https://papers.trelvimo.net/sheet/q/7XrTbaLeZpMmQ2uWvd9HkCj4yNoEfsGi3lRtAz_pk/view?mode=shared

Please feel free to design the business cards however you feel best. I am happy to give some creative freedoms and then provide feedback from there.

Please then also create a letterhead to match the business card design

Colors

Designer to choose colors to be used in the design.

Requirements
Must have
• Must be a modern, elegant business card which looks very professional

```html
<!DOCTYPE html>
<html lang="en">
<head>
<meta charset="utf-8">
<title>Nurlo Stationery</title>
<link rel="stylesheet" href="https://fonts.googleapis.com/css2?family=Poppins:wght@400;500;700&display=swap">
<style>
  :root {
    --bg: #e6e6e6;
    --paper: #f4f4f4;
    --red: #d51c24;
    --black: #121212;
    --ink: #2a2a2a;
    --photo-a: #8a8f7c;
    --photo-b: #3b3b3b;
  }
  * { margin: 0; padding: 0; box-sizing: border-box; }
  html, body { width: 1200px; height: 1019px; overflow: hidden; }
  body {
    position: relative;
    background: var(--bg);
    font-family: "Poppins", Arial, sans-serif;
    color: var(--ink);
  }

  /* Letterhead */
  .letterhead {
    position: absolute; left: 208px; top: 158px;
    width: 526px; height: 698px;
    background: var(--paper);
    overflow: hidden;
  }
  .letterhead__band { position: absolute; left: 0; top: 0; }
  .letterhead__name {
    position: absolute; left: 37px; top: 40px;
    font-size: 44px; font-weight: 700; letter-spacing: 2px;
    color: var(--red); line-height: 1;
  }
  .letterhead__heading {
    position: absolute; left: 35px; top: 188px;
    font-size: 14.5px; font-weight: 400; color: var(--black);
  }
  .letterhead__body {
    position: absolute; left: 35px; top: 243px; width: 458px;
    font-size: 7.9px; line-height: 10.6px; text-align: justify;
    color: var(--ink);
  }
  .letterhead__body p { margin-bottom: 10.6px; }
  .letterhead__signature {
    position: absolute; left: 390px; top: 528px;
    width: 100px; height: 32px;
    background: linear-gradient(90deg, #d8d8d8, #c9c9c9);
    border-radius: 3px;
  }
  .letterhead__contacts {
    position: absolute; left: 38px; top: 625px;
    list-style: none; font-size: 8.5px; line-height: 12px; color: var(--black);
  }
  .letterhead__contacts li { display: flex; align-items: center; gap: 6px; }
  .letterhead__address {
    position: absolute; right: 34px; top: 646px;
    font-size: 7px; line-height: 9.5px; text-align: right; color: var(--black);
  }
  .letterhead__foot {
    position: absolute; left: 0; bottom: 0; width: 100%; height: 13px;
    background: var(--black);
  }
  .icon { width: 8px; height: 8px; fill: var(--red); flex: none; }

  /* Business card front */
  .card {
    position: absolute; left: 800px; width: 246px; height: 138px;
    background: var(--black); overflow: hidden;
  }
  .card--front { top: 507px; display: flex; align-items: center; justify-content: center; }
  .card__name {
    font-size: 38px; font-weight: 700; letter-spacing: 2px;
    color: var(--red); line-height: 1; margin-top: 4px;
  }

  /* Business card back */
  .card--back { top: 718px; }
  .card__shape { position: absolute; left: 0; top: 0; }
  .card__person {
    position: absolute; left: 17px; top: 22px; color: var(--black);
  }
  .card__person-name { font-size: 10px; font-weight: 500; line-height: 12px; }
  .card__person-role { font-size: 6.6px; line-height: 8px; }
  .card__address {
    position: absolute; left: 17px; top: 57px;
    font-size: 6.6px; line-height: 9px; color: var(--black);
  }
  .card__contacts {
    position: absolute; left: 16px; top: 88px;
    list-style: none; font-size: 6.6px; line-height: 11px; color: var(--black);
  }
  .card__contacts li { display: flex; align-items: center; gap: 5px; }
  .card__contacts .icon { width: 6px; height: 6px; fill: var(--black); }
  .card__photo {
    position: absolute; left: 124px; top: 21px;
    width: 100px; height: 100px; border-radius: 50%;
    border: 3px solid var(--red);
    background: radial-gradient(circle at 50% 45%, var(--photo-a), var(--photo-b));
  }
</style>
</head>
<body>

  <section class="letterhead">
    <svg class="letterhead__band" width="526" height="122" viewBox="0 0 526 122" aria-hidden="true">
      <rect x="0" y="0" width="526" height="13" fill="#d51c24"/>
      <polygon points="280,13 526,13 526,121" fill="#d51c24"/>
    </svg>
    <div class="letterhead__name">NURLO</div>

    <h1 class="letterhead__heading">Lorem Ipsum</h1>

    <div class="letterhead__body">
      <p>Lorem ipsum dolor sit amet, consectetur adipiscing elit, sed do eiusmod tempor incididunt ut labore et dolore magna aliqua. In iaculis nunc sed augue lacus viverra vitae congue. Tempor orci eu lobortis elementum nibh tellus molestie. Nisl pretium fusce id velit ut. Platea dictumst vestibulum rhoncus est pellentesque elit ullamcorper. Laoreet id donec ultrices tincidunt arcu non. Turpis egestas maecenas pharetra convallis posuere morbi. Massa vitae tortor condimentum lacinia. Suspendisse interdum consectetur libero id. Proin fermentum leo vel orci porta non. Sed id semper risus in hendrerit gravida rutrum quisque non. Sagittis vitae et leo duis ut diam quam nulla. Amet justo donec enim diam vulputate ut. Diam donec adipiscing tristique risus nec feugiat in fermentum. Facilisis leo vel fringilla est. Tempor commodo ullamcorper a lacus vestibulum sed arcu non. Magna etiam tempor orci eu lobortis elementum nibh tellus.</p>
      <p>Massa sapien faucibus et molestie ac feugiat sed lectus vestibulum. Pellentesque adipiscing commodo elit at imperdiet dui accumsan sit. Bibendum neque egestas congue quisque egestas diam in arcu cursus. Nisi quis eleifend quam adipiscing vitae proin. Placerat vestibulum lectus mauris ultrices eros in cursus. Dolor sit amet consectetur adipiscing elit duis. Malesuada proin libero nunc consequat interdum varius sit amet mattis. Pretium vulputate sapien nec sagittis aliquam malesuada bibendum arcu. Morbi tristique senectus et netus et malesuada. Malesuada bibendum arcu vitae elementum curabitur vitae nunc. Amet volutpat consequat mauris nunc congue nisi vitae suscipit. Tincidunt ornare massa eget egestas purus viverra accumsan in. Risus in hendrerit gravida rutrum quisque non tellus orci. Fermentum leo vel orci porta.</p>
      <p>Sit amet facilisis magna etiam. Massa enim nec dui nunc mattis enim ut tellus. Ut placerat orci nulla pellentesque dignissim enim sit amet. Duis ut diam quam nulla porttitor massa. Ut porttitor leo a diam sollicitudin tempor. Felis eget velit aliquet sagittis. Fringilla phasellus faucibus scelerisque eleifend donec pretium vulputate sapien nec. Cursus metus aliquam eleifend mi in nulla. Euismod lacinia at quis risus sed vulputate odio ut. Tellus orci ac auctor augue mauris augue neque gravida. Consectetur adipiscing elit duis tristique sollicitudin nibh sit amet. Id donec ultrices tincidunt arcu. Vestibulum sed arcu non odio euismod lacinia. Pharetra et ultrices neque ornare aenean.</p>
    </div>

    <div class="letterhead__signature" role="img" aria-label="Handwritten signature"></div>

    <ul class="letterhead__contacts">
      <li><svg class="icon" viewBox="0 0 10 10" aria-hidden="true"><path d="M2 1h2l1 2.5-1.3 1a5.5 5.5 0 0 0 2.8 2.8l1-1.3L10 7v2a1 1 0 0 1-1 1A9 9 0 0 1 0 2a1 1 0 0 1 1-1z"/></svg>0491 570 318</li>
      <li><svg class="icon" viewBox="0 0 10 10" aria-hidden="true"><path d="M0 2h10v6H0z"/><path d="M0 2l5 3.5L10 2" fill="none" stroke="#f4f4f4" stroke-width="1"/></svg>liam@nurlo.com</li>
      <li><svg class="icon" viewBox="0 0 10 10" aria-hidden="true"><circle cx="5" cy="5" r="4.5"/><path d="M0.5 5h9M5 0.5c-2.5 2.5-2.5 6.5 0 9M5 0.5c2.5 2.5 2.5 6.5 0 9" fill="none" stroke="#f4f4f4" stroke-width="0.7"/></svg>www.nurlo.com</li>
    </ul>
    <address class="letterhead__address" style="font-style:normal">PO Box 3170<br>Brenfield NSW 2790</address>

    <div class="letterhead__foot"></div>
  </section>

  <section class="card card--front">
    <div class="card__name">NURLO</div>
  </section>

  <section class="card card--back">
    <svg class="card__shape" width="246" height="138" viewBox="0 0 246 138" aria-hidden="true">
      <polygon points="0,0 110,0 236,138 0,138" fill="#d51c24"/>
    </svg>
    <div class="card__person">
      <div class="card__person-name">Liam Corrow</div>
      <div class="card__person-role">Licenced Real Estate Agent</div>
    </div>
    <address class="card__address" style="font-style:normal">PO Box 3170<br>Brenfield NSW 2790</address>
    <ul class="card__contacts">
      <li><svg class="icon" viewBox="0 0 10 10" aria-hidden="true"><path d="M2 1h2l1 2.5-1.3 1a5.5 5.5 0 0 0 2.8 2.8l1-1.3L10 7v2a1 1 0 0 1-1 1A9 9 0 0 1 0 2a1 1 0 0 1 1-1z"/></svg>0491 570 318</li>
      <li><svg class="icon" viewBox="0 0 10 10" aria-hidden="true"><path d="M0 2h10v6H0z"/></svg>liam@nurlo.com</li>
      <li><svg class="icon" viewBox="0 0 10 10" aria-hidden="true"><circle cx="5" cy="5" r="4.5"/></svg>www.nurlo.com</li>
    </ul>
    <div class="card__photo" role="img" aria-label="Portrait photo of the agent"></div>
  </section>

</body>
</html>
```